Young and modern Electrical company working in the commercial arena.

Wanting a business card design thats modern and will last. Maybe Minimalist? Happy to look at changing my logo

Target Market(s)

Builders, Project Managers

Industry/Entity Type

Electrical

Contact Information for Business Card

Name
Address
Phone number
Job title

Logo Text

our name or just the logo i'm open to ideas

Font styles to use
Sans Serif

Requirements
Nice to have
• would like to keep the purple in our current logo. it's kinda unique to our market
Should not have
• Don't want it to be to busy. simple is best i think

```html
<!DOCTYPE html>
<html lang="en">
<head>
<meta charset="utf-8">
<title>Hadley Electrical – Business Card</title>
<link href="https://fonts.googleapis.com/css2?family=Arimo:wght@400&display=swap" rel="stylesheet">
<style>
  :root {
    --backdrop: #ece9e4;
    --purple: #6a43c0;
    --purple-deep: #5a34b0;
    --purple-light: #8a66d6;
    --purple-faint: #a58ce0;
    --band-white: #f1f1f3;
    --band-grey: #d9d9de;
    --ink-grey: #4e4e52;
    --label-white: #ffffff;
    --rule: rgba(255,255,255,0.45);
  }
  * { margin: 0; padding: 0; box-sizing: border-box; }
  html, body {
    width: 1200px; height: 1023px; overflow: hidden;
    background: var(--backdrop);
    font-family: "Arimo", Arial, sans-serif;
  }
  .canvas {
    position: relative; width: 1200px; height: 1023px;
  }
  .card {
    position: absolute; left: 250px; width: 700px; height: 400px;
    border-radius: 6px; overflow: hidden;
    box-shadow: 0 10px 30px rgba(60,40,90,0.25);
  }
  .card--front { top: 70px; }
  .card--back { top: 553px; }
  .card svg { position: absolute; inset: 0; width: 100%; height: 100%; }

  .front-brand {
    position: absolute; left: 90px; top: 150px;
    display: flex; align-items: center; gap: 20px;
  }
  .brand-dot {
    width: 56px; height: 56px; border-radius: 50%;
    border: 3px solid var(--ink-grey);
  }
  .brand-name {
    font-size: 50px; color: var(--ink-grey); font-weight: 400;
    letter-spacing: 0.5px;
  }

  .contact {
    position: absolute; top: 300px;
    color: var(--label-white); font-size: 15px; line-height: 22px;
    padding-top: 10px; border-top: 1px solid var(--rule); width: 240px;
  }
  .contact--person { left: 90px; }
  .contact--reach { left: 400px; }

  .back-brand {
    position: absolute; inset: 0;
    display: flex; align-items: center; justify-content: center;
  }
  .back-ring {
    position: absolute; width: 300px; height: 300px; border-radius: 50%;
    border: 6px solid var(--purple-faint); opacity: 0.7;
    left: 200px; top: 50px;
  }
  .back-name {
    position: relative; font-size: 42px; color: var(--purple-faint);
  }
</style>
</head>
<body>
<main class="canvas">

  <section class="card card--front" aria-label="Business card front">
    <svg viewBox="0 0 700 400" preserveAspectRatio="none" aria-hidden="true">
      <defs>
        <linearGradient id="purpleFill" x1="0" y1="0" x2="0" y2="1">
          <stop offset="0" stop-color="var(--purple-light)"/>
          <stop offset="1" stop-color="var(--purple-deep)"/>
        </linearGradient>
        <linearGradient id="bandFill" x1="0" y1="0" x2="0" y2="1">
          <stop offset="0" stop-color="var(--band-grey)"/>
          <stop offset="0.3" stop-color="var(--band-white)"/>
          <stop offset="0.7" stop-color="var(--band-white)"/>
          <stop offset="1" stop-color="var(--band-grey)"/>
        </linearGradient>
      </defs>
      <rect width="700" height="400" fill="url(#purpleFill)"/>
      <polygon points="0,45 95,110 605,110 700,45 700,330 605,275 95,275 0,330" fill="url(#bandFill)"/>
      <polygon points="0,45 95,110 95,275 0,330" fill="#ffffff" opacity="0.6"/>
      <polygon points="700,45 605,110 605,275 700,330" fill="#ffffff" opacity="0.6"/>
    </svg>

    <div class="front-brand">
      <span class="brand-dot"></span>
      <span class="brand-name">Hadley Electrical</span>
    </div>

    <div class="contact contact--person">
      <div>Name</div>
      <div>Job Title</div>
    </div>
    <div class="contact contact--reach">
      <div>Address</div>
      <div>Phone No.</div>
    </div>
  </section>

  <section class="card card--back" aria-label="Business card back">
    <svg viewBox="0 0 700 400" preserveAspectRatio="none" aria-hidden="true">
      <defs>
        <radialGradient id="backFill" cx="0.5" cy="0.5" r="0.7">
          <stop offset="0" stop-color="var(--purple-light)"/>
          <stop offset="1" stop-color="var(--purple)"/>
        </radialGradient>
      </defs>
      <rect width="700" height="400" fill="url(#backFill)"/>
    </svg>
    <div class="back-brand">
      <span class="back-ring"></span>
      <span class="back-name">Hadley Electrical</span>
    </div>
  </section>

</main>
</body>
</html>
```